Icons/images for company values

We have five company values, we have a new logo and a new look. I would like drawn images for each value that are in keeping with our look and feel.

Target Market(s)

internal/staff

Industry/Entity Type

media compliance

Requirements
Must have
• colours aligned with logo.

```html
<!DOCTYPE html>
<html lang="en">
<head>
<meta charset="utf-8">
<title>Values 2023</title>
<link rel="stylesheet" href="https://fonts.googleapis.com/css2?family=Poppins:wght@400;800&family=Questrial&display=swap">
<style>
  :root {
    --page-bg: #ececec;
    --paper: #ffffff;
    --navy: #3d6a8f;
    --ink: #1f2630;
    --open: #3b6a91;
    --faster: #5a9fc8;
    --leaders: #7ecbb0;
    --done: #9ccf9c;
    --diverse: #a8972a;
    --rule: #9fb4c6;
    --ring: #b9cbd8;
  }
  * { margin: 0; padding: 0; box-sizing: border-box; }
  html, body { width: 707px; height: 1200px; overflow: hidden; background: var(--page-bg); }
  .poster {
    position: absolute; left: 0; top: 327px; width: 707px; height: 546px;
    background: var(--paper); box-shadow: 0 8px 24px rgba(0,0,0,0.18); overflow: hidden;
  }
  .poster-inner {
    position: absolute; left: 0; top: 0; width: 1328px; height: 1026px;
    transform: scale(0.5324); transform-origin: 0 0;
  }
  .wheel { position: absolute; left: 0; top: 0; width: 1328px; height: 1026px; }
  .brand {
    position: absolute; left: 66px; top: 194px;
    font-family: "Questrial", sans-serif; font-size: 36px; letter-spacing: 8px;
    line-height: 1; color: var(--navy); white-space: nowrap;
  }
  .badge-label {
    position: absolute; left: 127px; width: 330px; text-align: center; color: #fff;
    font-family: "Questrial", sans-serif; line-height: 1;
  }
  .badge-label.word { top: 432px; font-size: 60px; }
  .badge-label.year { top: 485px; font-size: 92px; }
  .value { position: absolute; }
  .value h2 {
    font-family: "Poppins", sans-serif; font-weight: 800; font-size: 29px;
    line-height: 34px; letter-spacing: 0.3px; text-transform: uppercase; white-space: nowrap;
  }
  .value p {
    font-family: "Poppins", sans-serif; font-weight: 400; font-size: 20px;
    line-height: 24px; color: var(--ink); margin-top: 4px; white-space: nowrap;
  }
  .value.open { left: 518px; top: 90px; }
  .value.open h2 { color: var(--open); }
  .value.faster { left: 684px; top: 245px; }
  .value.faster h2 { color: var(--faster); }
  .value.leaders { left: 735px; top: 433px; }
  .value.leaders h2 { color: var(--leaders); }
  .value.leaders p { margin-top: 14px; }
  .value.done { left: 684px; top: 688px; }
  .value.done h2 { color: var(--done); }
  .value.diverse { left: 518px; top: 838px; }
  .value.diverse h2 { color: var(--diverse); }
  .rule { position: absolute; height: 0; border-top: 1px dotted var(--rule); }
</style>
</head>
<body>
<div class="poster">
  <div class="poster-inner">
    <svg class="wheel" viewBox="0 0 1328 1026" xmlns="http://www.w3.org/2000/svg">
      <defs>
        <linearGradient id="seg-open" x1="0" y1="1" x2="1" y2="0">
          <stop offset="0" stop-color="#3a6587"/><stop offset="1" stop-color="#4a7fb8"/>
        </linearGradient>
        <linearGradient id="seg-faster" x1="0" y1="0" x2="1" y2="1">
          <stop offset="0" stop-color="#5a98d2"/><stop offset="1" stop-color="#6cb6b2"/>
        </linearGradient>
        <linearGradient id="seg-leaders" x1="0" y1="0" x2="0" y2="1">
          <stop offset="0" stop-color="#6dbfb2"/><stop offset="1" stop-color="#92dba6"/>
        </linearGradient>
        <linearGradient id="seg-done" x1="1" y1="0" x2="0" y2="1">
          <stop offset="0" stop-color="#99d891"/><stop offset="1" stop-color="#dfe06a"/>
        </linearGradient>
        <linearGradient id="seg-diverse" x1="0" y1="0" x2="1" y2="1">
          <stop offset="0" stop-color="#f0dc5c"/><stop offset="1" stop-color="#f0d85a"/>
        </linearGradient>
      </defs>

      <g class="connector" fill="none" stroke="var(--navy)" stroke-width="3">
        <circle cx="80" cy="335" r="8"/>
        <polyline points="80,343 80,770 269,770"/>
        <circle cx="277" cy="770" r="8"/>
      </g>

      <g class="segments" stroke="#fff" stroke-width="14" stroke-linejoin="miter">
        <path fill="url(#seg-open)" d="M292,140 A360,360 0 0 1 503.7,208.8 L409.6,338.2 A200,200 0 0 0 292,300 Z"/>
        <path fill="url(#seg-faster)" d="M503.7,208.8 A360,360 0 0 1 634.4,388.8 L482.2,438.2 A200,200 0 0 0 409.6,338.2 Z"/>
        <path fill="url(#seg-leaders)" d="M634.4,388.8 A360,360 0 0 1 634.4,611.2 L482.2,561.8 A200,200 0 0 0 482.2,438.2 Z"/>
        <path fill="url(#seg-done)" d="M634.4,611.2 A360,360 0 0 1 503.7,791.2 L409.6,661.8 A200,200 0 0 0 482.2,561.8 Z"/>
        <path fill="url(#seg-diverse)" d="M503.7,791.2 A360,360 0 0 1 292,860 L292,700 A200,200 0 0 0 409.6,661.8 Z"/>
      </g>

      <circle cx="292" cy="500" r="196" fill="#fff" stroke="var(--ring)" stroke-width="1.5"/>
      <circle cx="292" cy="500" r="166" fill="var(--navy)"/>

      <g class="icon-trophy" transform="translate(378,234)" fill="#fff">
        <path d="M-32,-38 H32 V-12 C32,8 18,20 0,22 C-18,20 -32,8 -32,-12 Z"/>
        <path d="M-32,-32 H-44 V-20 C-44,-6 -34,2 -26,4" fill="none" stroke="#fff" stroke-width="6"/>
        <path d="M32,-32 H44 V-20 C44,-6 34,2 26,4" fill="none" stroke="#fff" stroke-width="6"/>
        <rect x="-6" y="20" width="12" height="16"/>
        <rect x="-18" y="34" width="36" height="8"/>
        <rect x="-26" y="42" width="52" height="8"/>
        <polygon fill="var(--navy)" points="0,-28 4,-18 14,-18 6,-11 9,-1 0,-7 -9,-1 -6,-11 -14,-18 -4,-18"/>
      </g>

      <g class="icon-speed" transform="translate(518,335)" fill="none" stroke="#fff" stroke-width="5">
        <circle cx="0" cy="0" r="22"/>
        <line x1="0" y1="-22" x2="0" y2="-30"/>
        <line x1="-6" y1="-31" x2="6" y2="-31"/>
        <polyline points="0,-12 0,0 9,6"/>
        <path d="M-30,-14 A34,34 0 0 1 28,-24"/>
        <polyline points="22,-36 30,-24 16,-20"/>
        <path d="M30,14 A34,34 0 0 1 -28,24"/>
        <polyline points="-22,36 -30,24 -16,20"/>
      </g>

      <g class="icon-idea" transform="translate(572,496)">
        <circle cx="0" cy="0" r="27" fill="#fff"/>
        <polyline points="-11,0 -3,8 12,-8" fill="none" stroke="#6dbfb2" stroke-width="5"/>
        <g fill="#fff">
          <rect x="-14" y="32" width="28" height="5"/>
          <rect x="-14" y="41" width="28" height="5"/>
          <rect x="-10" y="50" width="20" height="5"/>
        </g>
        <g stroke="#fff" stroke-width="5">
          <line x1="0" y1="-36" x2="0" y2="-46"/>
          <line x1="-36" y1="0" x2="-46" y2="0"/>
          <line x1="36" y1="0" x2="46" y2="0"/>
          <line x1="-26" y1="-26" x2="-33" y2="-33"/>
          <line x1="26" y1="-26" x2="33" y2="-33"/>
          <line x1="-26" y1="26" x2="-33" y2="33"/>
          <line x1="26" y1="26" x2="33" y2="33"/>
        </g>
      </g>

      <g class="icon-capability" transform="translate(515,660)">
        <circle cx="4" cy="-16" r="24" fill="none" stroke="#fff" stroke-width="10" stroke-dasharray="8 5"/>
        <circle cx="4" cy="-16" r="18" fill="none" stroke="#fff" stroke-width="5"/>
        <circle cx="4" cy="-16" r="7" fill="none" stroke="#fff" stroke-width="4"/>
        <path fill="#fff" d="M-30,10 H26 V44 H-22 V34 H-30 Z"/>
      </g>

      <g class="icon-together" transform="translate(372,772)">
        <g fill="#fff">
          <rect x="-12" y="-46" width="24" height="10" rx="2"/>
          <rect x="-9" y="-34" width="18" height="8"/>
          <rect x="-17" y="-26" width="7" height="34" rx="3.5"/>
          <rect x="-8.5" y="-28" width="7" height="38" rx="3.5"/>
          <rect x="1.5" y="-28" width="7" height="38" rx="3.5"/>
          <rect x="10" y="-26" width="7" height="34" rx="3.5"/>
        </g>
        <g fill="none" stroke="#fff" stroke-width="13" stroke-linecap="round">
          <path d="M-14,6 C-16,16 -24,24 -34,30"/>
          <path d="M14,6 C16,16 24,24 34,30"/>
        </g>
        <g fill="#fff">
          <rect x="-54" y="28" width="20" height="12" rx="2" transform="rotate(-35 -44 34)"/>
          <rect x="34" y="28" width="20" height="12" rx="2" transform="rotate(35 44 34)"/>
        </g>
      </g>
    </svg>

    <div class="brand">LUMORA</div>
    <div class="badge-label word">VALUES</div>
    <div class="badge-label year">2023</div>

    <section class="value open">
      <h2>We're open and honest</h2>
      <p>Sharing information helps us achieve the best outcomes for our teams<br>and business. We value open, honest, and clear communication.</p>
    </section>
    <div class="rule" style="left:618px; top:206px; width:592px;"></div>

    <section class="value faster">
      <h2>We get&nbsp; there faster together</h2>
      <p>Collaboration is at the heart of what we do, no<br>matter our team</p>
    </section>
    <div class="rule" style="left:672px; top:383px; width:538px;"></div>

    <section class="value leaders">
      <h2>We are leaders in copyright<br>and intellectual property</h2>
      <p>Leading the conversation in audio-visual<br>copyright compliance and advocating for<br>the protection of intellectual property globally.</p>
    </section>
    <div class="rule" style="left:672px; top:647px; width:538px;"></div>

    <section class="value done">
      <h2>We get things done</h2>
      <p>We grow through capability, focus and hard work. We<br>believe small steps compound to big results.</p>
    </section>
    <div class="rule" style="left:608px; top:810px; width:602px;"></div>

    <section class="value diverse">
      <h2>Diverse perspectives build better outcomes</h2>
      <p>We value diversity, inclusion, respect and trust within our teams. We are<br>building a truly global organisation.</p>
    </section>
  </div>
</div>
</body>
</html>
```